Lantern Pantry cafe promotion flyer

Lantern Pantry is a waterfront cafe/ function center with gorgeous views. Lantern Pantry is a very modern venue that can cater for 200 people (seating) and it is located in a business area.

The main customers are the professional bank employees (80%) with the remaining being other corporate workers. Lantern Pantrys main trading periods are Morning Coffee, Breakfast and Lunch with the average spend being between $5-$15 per head. Hospitality is a highly competitive market and since there is not much general foot traffic on the waterfront side during winter, Lantern Pantry have decided to advertise by sending out some flyers to all the nearby buildings, to let the Quayview Community know where we are, what we offer and to generate new business.

We would like to design a unique flyer with a great title, plus the deals we offer, plus some pictures , would prefer fresh and bright colour which can attract people from outside the venue .You can visit our website and have a look at our venue to get some idea as well:
www.thelanternpantry.com.au

Thanks for the designs submitted so far.
but I prefer the background color is bight color, like fresh food color will be better, prefer orange, green, yellow that kind of fresh color, can entice people to come in and have their lunch or breakfast.

I would prefer to have a picture of coffee with coffee art, food change to a big sandwich or burger. The entire flyer is try to entice the customer to come in eat and drink. The flyer is going to be put on a black board, so there should be some contrast in the colour.

look forward to your new design.

Here is a sample title:
only our special offers warm up your savings

(or something similar, more creative and appealing to the potential customers)

Monday-Friday, early bird coffee 7:30a-8:30am, small for $2.80, large for $3.30.

Deals detail:
coffee with freshly home-made muffin $5.50
Coffee with egg bacon muffin $6.90
Coffee with gourmet egg bacon wrap $8.50
Coffee with fruit toast $6.50

Lunch Special:
Only $4 for a glass of wine/a bottle of beer with our daily Lunch specail
Buy any Focaccia for only $8.90 get one soft drink free

Friday Happy hour drinks 12pm-7pm,
selection of wine/beer/spirits for only $6

corporate catering and function room hire available
Waterfront Side, QRT building, 415 Tillard Street, Docklands 3008
E:catering@thelanternpantry.com.au
P:03 9482 3157

we require hi resolution PDF files of both A5 and A3 Poster

                                       

Hi all designers

but I prefer the background color  is bight color, like fresh food color will be better, prefer orange, green, yellow that kind of fresh color, can entice people to come in and have their lunch or breakfast.

I would prefer to change the coffee to a coffee with coffee art, food change to a better sandwich or burger or focaccia. The entire flyer is try to entice the customer to come in eat and drink.

will you be able to add this to it:

Also, can you please take away the live band 4p-7pm for Fridays , thanks.

the target customers are the corporates who has something quick to eat for breakfast and lunch, normally on a budget.

Catering

Must have
• great food and drink pictures
Should not have
• dark colour

```html
<!DOCTYPE html>
<html lang="en">
<head>
<meta charset="utf-8">
<title>Lantern Pantry – Winter Special Offers</title>
<link href="https://fonts.googleapis.com/css2?family=Lobster&family=Source+Sans+3:ital,wght@0,400;0,700;1,700&display=swap" rel="stylesheet">
<style>
  :root {
    --brick: #b5301d;
    --brick-deep: #a82a18;
    --salmon: #f59a80;
    --coral: #d8664b;
    --lemon: #e9ef2a;
    --white: #ffffff;
    --leaf: #5fae2e;
    --wine: #6b1f33;
    --wood: #9a7c5c;
  }
  * { margin: 0; padding: 0; box-sizing: border-box; }
  html, body { width: 915px; height: 1200px; overflow: hidden; background: #f4f4f4; }
  .flyer {
    position: relative;
    width: 915px;
    height: 1200px;
    overflow: hidden;
    background: linear-gradient(100deg, var(--brick-deep) 0%, var(--coral) 35%, var(--salmon) 58%, var(--coral) 75%, var(--brick) 100%);
    font-family: "Source Sans 3", sans-serif;
    color: var(--white);
  }
  .hero-photo {
    position: absolute; left: 0; top: 0; width: 915px; height: 552px;
    background:
      radial-gradient(ellipse at 12% 18%, var(--leaf) 0%, rgba(95,174,46,0) 45%),
      radial-gradient(ellipse at 88% 30%, #d8352a 0%, rgba(216,53,42,0) 35%),
      radial-gradient(ellipse at 22% 55%, var(--wine) 0%, rgba(107,31,51,0) 40%),
      linear-gradient(180deg, #7fb24a 0%, #b3977a 55%, var(--wood) 100%);
  }
  .brand-name {
    position: absolute; left: 0; top: 108px; width: 915px; text-align: center;
    font-family: "Lobster", sans-serif; font-size: 64px; line-height: 80px; color: var(--lemon);
  }
  .early-bird {
    position: absolute; left: 50%; top: 214px; transform: translateX(-50%);
    white-space: nowrap;
    padding: 6px 20px; border-radius: 20px;
    background: rgba(168, 42, 24, 0.82);
    font-size: 21px; line-height: 28px; font-weight: 700; color: var(--white);
  }
  .early-bird .accent { color: var(--lemon); }
  .headline-box {
    position: absolute; left: 66px; top: 293px; width: 786px; height: 229px;
    border-radius: 22px;
    background: rgba(180, 50, 35, 0.72);
    display: flex; align-items: center; justify-content: center;
  }
  .headline {
    font-family: "Lobster", sans-serif; font-weight: 400;
    font-size: 47px; line-height: 64px; text-align: center; color: var(--white);
  }
  .offers { position: absolute; left: 26px; top: 560px; list-style: none; }
  .offers li {
    font-family: "Lobster", sans-serif; font-size: 35px; line-height: 48px; color: var(--lemon);
  }
  .offers .price { color: var(--white); }
  .section-title {
    position: absolute; left: 24px; top: 766px;
    font-family: "Lobster", sans-serif; font-weight: 400; font-size: 42px; line-height: 56px; color: var(--white);
  }
  .lunch-drinks {
    position: absolute; left: 26px; top: 834px; width: 760px;
    font-size: 27px; line-height: 33px;
  }
  .focaccia {
    position: absolute; left: 26px; top: 905px; width: 530px;
    font-size: 25px; line-height: 33px; font-weight: 700; font-style: italic;
  }
  .friday-title {
    position: absolute; left: 22px; top: 972px;
    font-family: "Lobster", sans-serif; font-weight: 400; font-size: 34px; line-height: 44px; color: var(--lemon);
  }
  .friday-list { position: absolute; left: 22px; top: 1018px; list-style: none; }
  .friday-list li { font-size: 22px; line-height: 28px; color: var(--lemon); }
  .friday-list .big { font-weight: 700; font-size: 28px; color: var(--white); }
  .friday-list .group { color: var(--white); }
  .contact {
    position: absolute; left: 22px; top: 1138px; width: 520px;
    font-size: 15px; line-height: 19px; color: var(--white);
  }
  .contact strong { color: var(--lemon); }
  .diners-photo { position: absolute; left: 556px; top: 864px; }
</style>
</head>
<body>
  <div class="flyer">
    <div class="hero-photo" role="img" aria-label="Glass of red wine beside a fresh salad with tomatoes on a wooden table"></div>

    <div class="brand-name">Lantern Pantry</div>

    <p class="early-bird">Mon–Fri Early Bird Coffee 7:30–8:30am · <span class="accent">Small $2.80 · Large $3.30</span></p>

    <div class="headline-box">
      <h1 class="headline">This winter is not so cold with<br>Lantern Pantry's<br>Special Offers</h1>
    </div>

    <ul class="offers">
      <li>Coffee with freshly home-made muffin <span class="price">$5.50</span></li>
      <li>Coffee with egg bacon muffin <span class="price">$6.90</span></li>
      <li>Coffee with gourmet egg bacon wrap <span class="price">$8.50</span></li>
      <li>Coffee with fruit toast <span class="price">$6.50</span></li>
    </ul>

    <h2 class="section-title">Lunch Special:</h2>
    <p class="lunch-drinks"><strong>ONLY $4</strong> for a glass of wine/a bottle of beer with our daily<br>Lunch Special</p>
    <p class="focaccia">Buy any Focaccia for only $8.90 get one<br>soft drink FREE</p>

    <h2 class="friday-title">Friday Afternoon</h2>
    <ul class="friday-list">
      <li><strong><em>Happy Hour</em></strong> drink 12pm-7pm</li>
      <li>Selection of wine/beer/spirits for <span class="big">only $6</span></li>
      <li class="group">Any group booking 8+ for breakfast /lunch<br>will get <strong>10% discount</strong></li>
    </ul>

    <div class="contact">
      <p><strong>Corporate catering &amp; function room hire available</strong></p>
      <p>Waterfront Side, QRT building, 415 Tillard Street, Docklands 3008</p>
      <p>E: catering@thelanternpantry.com.au &nbsp; P: 03 9482 3157</p>
    </div>

    <svg class="diners-photo" width="324" height="324" viewBox="0 0 324 324" role="img" aria-label="Couple enjoying a glass of red wine at a cafe table">
      <defs>
        <radialGradient id="dinersTone" cx="0.55" cy="0.45" r="0.6">
          <stop offset="0" stop-color="#efe6da"/>
          <stop offset="0.6" stop-color="#a9896a"/>
          <stop offset="1" stop-color="#5a4636"/>
        </radialGradient>
      </defs>
      <circle cx="162" cy="162" r="158" fill="url(#dinersTone)" stroke="#ffffff" stroke-width="5"/>
    </svg>
  </div>
</body>
</html>
```